Moltven Advisory e-Flyer Design

Need 6 or so one pagers done. To be used to email to clients. Each to look similar with slight variations. Attached is an example done for a completely different organization, but it has the style we are looking for, and it is energetic and corporate.

```html
<!DOCTYPE html>
<html lang="en">
<head>
<meta charset="utf-8">
<title>Moltven Advisory – Services Flyer</title>
<link href="https://fonts.googleapis.com/css2?family=PT+Sans+Narrow:wght@400;700&family=Source+Sans+3:wght@300;400;700&display=swap" rel="stylesheet">
<style>
  :root{
    --page-bg:#d9d9dc;
    --paper:#ffffff;
    --brand-red:#d2232a;
    --band-grey:rgba(180,180,184,0.92);
    --navy:#0c2a52;
    --green:#86b842;
    --ink:#2b2b2b;
    --white:#ffffff;
    --rule:rgba(255,255,255,0.55);
  }
  *{margin:0;padding:0;box-sizing:border-box}
  html,body{width:1200px;height:1200px;overflow:hidden;background:var(--page-bg)}
  .flyer{
    position:absolute;left:176px;top:0;width:847px;height:1200px;
    background:var(--paper);overflow:hidden;
    font-family:"PT Sans Narrow",sans-serif;color:var(--ink);
  }
  .hero-photo{
    position:absolute;left:326px;top:0;width:521px;height:442px;
    background:
      radial-gradient(ellipse at 85% 8%,rgba(255,226,160,0.95) 0%,rgba(230,170,90,0.55) 25%,rgba(0,0,0,0) 55%),
      linear-gradient(180deg,#b9ab96 0%,#8c7a66 35%,#4a3e36 65%,#2c2622 100%);
  }
  .title-band{
    position:absolute;left:0;top:50px;width:847px;height:92px;background:var(--band-grey);
  }
  .tagline{
    position:absolute;left:232px;top:67px;
    font-family:"PT Sans Narrow",sans-serif;font-weight:700;font-size:23px;line-height:31px;
    color:var(--white);text-transform:uppercase;letter-spacing:0.1px;
  }
  .brand-box{
    position:absolute;left:46px;top:29px;width:151px;height:142px;background:var(--brand-red);
    display:flex;align-items:center;justify-content:center;text-align:center;
  }
  .brand-name{
    font-family:"PT Sans Narrow",sans-serif;font-weight:400;font-size:27px;line-height:30px;
    color:var(--white);text-transform:uppercase;
  }
  .about{position:absolute;left:46px;top:190px;width:260px}
  .about h2{
    font-family:"Source Sans 3",sans-serif;font-weight:400;font-size:24px;line-height:28px;
    color:var(--brand-red);text-transform:uppercase;
  }
  .about p{font-size:9.6px;line-height:13.7px;margin-bottom:12px}
  .about .values{font-family:"Source Sans 3",sans-serif;font-size:18px;line-height:22px}
  .services{
    position:absolute;left:0;top:442px;width:847px;height:691px;background:var(--navy);
    padding:14px 45px 0 46px;color:var(--white);
  }
  .services > h2{
    font-family:"Source Sans 3",sans-serif;font-weight:400;font-size:24px;line-height:30px;
    padding-bottom:10px;border-bottom:1px dotted var(--rule);
  }
  .service{padding:4px 0 6px;border-bottom:1px dotted var(--rule)}
  .service:last-child{border-bottom:none}
  .service h3{
    font-family:"Source Sans 3",sans-serif;font-weight:400;font-size:25px;line-height:30px;color:var(--green);
  }
  .service .lead{font-size:18px;line-height:24px}
  .service ul{list-style:none;font-size:9.2px;line-height:13.6px;padding-left:12px}
  .service li{position:relative}
  .service li::before{content:"•";position:absolute;left:-11px}
  .contact-bar{
    position:absolute;left:0;top:1133px;width:847px;height:67px;
    display:flex;align-items:flex-start;justify-content:center;padding-top:12px;
    font-family:"Source Sans 3",sans-serif;font-weight:700;font-size:18.5px;color:var(--brand-red);
    text-transform:uppercase;
  }
</style>
</head>
<body>
<main class="flyer">
  <div class="hero-photo" role="img" aria-label="Photo of a busy city street at sunset, crowds of commuters walking between stone buildings in warm backlight"></div>
  <div class="title-band"></div>
  <p class="tagline">Moltven Advisory is unique global management consultancy.<br>We convert strategy into action, and action into results.</p>
  <div class="brand-box"><span class="brand-name">Moltven<br>Advisory</span></div>

  <section class="about">
    <h2>Who we are</h2>
    <p>Moltven Advisory operates in the US, Europe, Asia, Australia and New Zealand. The Moltven Advisory team consists of highly experienced corporate executives with a track record of delivering transformational programs to organizations across industries, both commercial and not for profit, large and small, to achieve higher performance.</p>
    <h2>Mission</h2>
    <p>To partner with organizations to ignite and empower them around a clear strategy, and facilitate efficient and fully integrated execution, to deliver higher performance.</p>
    <h2>Values</h2>
    <p class="values">Ignite, Empower, Deliver</p>
  </section>

  <section class="services">
    <h2>SERVICES</h2>
    <article class="service">
      <h3>Ignition</h3>
      <p class="lead">Ignite is a proven, proprietary method to bring cohesion to a team to create a shared understanding of what they want to achieve and how they will galvanize the organization to achieve it.</p>
      <ul>
        <li>Effective dialogue is the most productive way to truly harness the collective intellect of a team and organization.</li>
        <li>Moltven Advisory uses a tested process, Ignition, to create a space for great dialog for teams of up to 300 people.</li>
        <li>The Ignite process is tailored for each client to clarify strategy, define the execution path, strengthen team cohesion and ignite momentum.</li>
        <li>Ignition happens at speed to create a bridge for the present state to the future state.</li>
        <li>Ignition is purposely built to create ownership by the team.</li>
        <li>Ignition frequently produces breakthroughs and is about unleashing what a collective can achieve together.</li>
      </ul>
    </article>
    <article class="service">
      <h3>Strategy Clarification</h3>
      <p class="lead">Knowing what organization wants to be in 3-5 years time is a competitive advantage.</p>
      <ul>
        <li>Concisely exploring the alternatives and selecting on objective and strategy for the strategic horizon is a comparative advantage for organizations that undertake a proper strategic planning process including understanding evolving customer needs, competitive differentiation, and the critical capabilities required to compete and win.</li>
        <li>Research shows that organizations that are executing against a clear strategy outperform those that do not, even if the choice of strategy ultimately proves to be incorrect, largely due to deliberate intent and discipline.</li>
        <li>Having a 3-5 year strategy is critical to allowing the organization to have a coherent direction which all stakeholders can support, make strategic investments in future capabilities, and outperform the competition.</li>
      </ul>
    </article>
    <article class="service">
      <h3>Executional Alignment</h3>
      <p class="lead">Strategy is just an exercise unless it is executed effectively and becomes the operating blueprint of the organization.</p>
      <ul>
        <li>Strategy a critical starting point to set objective and direction for the 3 year horizon, however without the organization executing against strategy, it is academic.</li>
        <li>Driving executional alignment to the strategy is critical to success, and requires the organization to consciously align the operations of the business to the strategy.</li>
        <li>Executional alignment requires overcoming the inertia of Business as Usual by enabling change through all aspects of the organization, identifying and removing barriers, beginning with a culture of embracing the strategy and competing to win.</li>
      </ul>
    </article>
    <article class="service">
      <h3>Leadership Development</h3>
      <p class="lead">Having the right leadership capability is the difference between success and failure.</p>
      <ul>
        <li>Every organization is comprised of unique people with different styles, experience and expertise.</li>
        <li>Ensuring leaders at all levels of the organization are suitably developed and equipped to do the best job is critical to outperform the competition and being on employer of choice to retain talented employees.</li>
        <li>The skills of leadership are evolving with changing demographics, technology, increased understanding of the benefits of diversity, a premium on innovation, amongst other macro trends, and organizations need to ensure their leaders have the knowledge and capabilities to manage these changes effectively.</li>
      </ul>
    </article>
    <article class="service">
      <h3>Cultural Transformation</h3>
      <p class="lead">Organizational culture can evolve organically, or it can be seen as a business asset that is consciously managed.</p>
      <ul>
        <li>Organizations that choose the culture they desire are leveraging one of the most important business assets available, one that is often to evolve without overt consideration.</li>
        <li>Placing clear focus on the desired culture and having initiative to achieve this, and monitoring performance against the intent, is a competitive differentiator.</li>
      </ul>
    </article>
  </section>

  <footer class="contact-bar">For more information: call +1 212 555 0147, email info@moltvenadvisory.com</footer>
</main>
</body>
</html>
```